Latvian local photo material wholesaler requires a Car Wrap Design for self-advertising

Car Wrap Design for Photo Materials Department

Design a captivating car wrap for our "white Brava Tolen 2020" that represents our photo materials department. We specialize in photo frames, albums, films, chemicals, and batteries, serving Latvian customers as a wholesaler. Our goal is to expand our reach to the Baltic States as well.

The design should be eye-catching and attention-grabbing, aimed at attracting bystanders. Please incorporate our logo into the wrap design if possible. Additionally, feel free to include a slogan related to providing clients with all their photo product needs.

For inspiration, visit our website [https://vexund.lv/en/] to understand our business and explore our photo products [https://vexund.lv/en/kategorijas/photo-materials/].

You can search for our photo department products here: https://ecom.vexund.lv/ecom/
Under "Photo Goods" which is located to the left side of the screen under "Categories". Picture quality might not be the best and some of the products might not have images, but it's to get the general idea.

Please note that the car wrap design should be "standalone" and focused specifically on our photo department.
Updates

Low designer entries for the paid expectation (50+). As this is the first time trying out the service, just now noticed the option to "guarantee the project", by agreeing that there won't be a refund. Please extend the project deadline, so that there is enough time for designers to submit their ideas. Thank you.

Target Market(s)

Target market are everyday customers. B2C oriented business

Font styles to use
Other font styles liked:
• Josefin Sans

Requirements
Must have
• Products that we sell (they don't have to be the exact ones, but just to show the idea what we sell): photo frames, albums, films (+ nice to have chemicals, batteries)
Nice to have
• A place where our products are listed.
Should not have
• Logo names of products, that we are not partnered with. Partners here: https://vexund.lv/en/about-us/

```html
<!DOCTYPE html>
<html lang="lv">
<head>
<meta charset="utf-8">
<title>Vexund photo department – car wrap panel</title>
<link rel="stylesheet" href="https://fonts.googleapis.com/css2?family=Poppins:ital,wght@0,600;0,700;1,700&display=swap">
<style>
  :root {
    --stage: #e6e7e9;
    --wrap-red: #741f28;
    --window-white: #fffdfb;
    --ink-maroon: #4a0f17;
    --dot-orange: #e8923a;
    --dot-peach: #f8d7a8;
    --url-white: #ffffff;
  }
  * { box-sizing: border-box; margin: 0; padding: 0; }
  html, body {
    width: 1200px;
    height: 800px;
    overflow: hidden;
    background: var(--stage);
  }
  .wrap-panel {
    position: absolute;
    left: 100px;
    top: 70px;
    width: 1000px;
    height: 660px;
    background: var(--wrap-red);
    border-radius: 28px;
    overflow: hidden;
  }
  .top-dots {
    position: absolute;
    left: 0; top: 0;
    width: 100%; height: 50px;
    background: radial-gradient(ellipse 45% 100% at 50% 0%, rgba(248,215,168,0.55), rgba(248,215,168,0) 100%);
  }
  .rear-window {
    position: absolute;
    left: 60px;
    top: 50px;
    width: 880px;
    height: 270px;
    background:
      radial-gradient(ellipse 40% 55% at 50% 20%, rgba(248,215,168,0.6), rgba(248,215,168,0) 100%),
      radial-gradient(ellipse 30% 50% at 55% 90%, rgba(248,215,168,0.45), rgba(248,215,168,0) 100%),
      var(--window-white);
    border-radius: 26px 26px 10px 10px;
  }
  .product-list {
    position: absolute;
    inset: 34px 40px;
    display: grid;
    grid-template-columns: 0.95fr 1.25fr 1.1fr;
    row-gap: 22px;
    list-style: none;
    font-family: "Poppins", sans-serif;
    font-weight: 700;
    font-size: 36px;
    line-height: 1.2;
    color: var(--ink-maroon);
    white-space: nowrap;
  }
  .product-list li::before { content: "›"; }
  .product-list .is-italic { font-style: italic; }
  .dot-field {
    position: absolute;
    left: 180px;
    top: 320px;
    width: 640px;
    height: 150px;
    background: radial-gradient(ellipse 50% 80% at 50% 10%, rgba(232,146,58,0.55), rgba(232,146,58,0) 100%);
  }
  .site-url {
    position: absolute;
    left: 0;
    bottom: 70px;
    width: 100%;
    text-align: center;
    font-family: "Poppins", sans-serif;
    font-weight: 700;
    font-size: 70px;
    letter-spacing: 7px;
    color: var(--url-white);
  }
</style>
</head>
<body>
  <main class="wrap-panel">
    <div class="top-dots" role="img" aria-label="Soft orange halftone dot pattern along the roof edge"></div>
    <section class="rear-window">
      <ul class="product-list">
        <li class="is-italic">Rāmji</li>
        <li>Fotokameras</li>
        <li>Foto albumi</li>
        <li class="is-italic">Papīrs</li>
        <li>Foto ķīmija</li>
        <li>Baterijas</li>
        <li class="is-italic">Statīvi</li>
        <li>Zibspuldzes</li>
        <li>Fotofilmas</li>
      </ul>
    </section>
    <div class="dot-field" role="img" aria-label="Orange halftone dot pattern fading below the window"></div>
    <p class="site-url">WWW.VEXUND.LV</p>
  </main>
</body>
</html>
```